Business Card Design Project

I need a business card design for my freelance solo makeup artistry business in Melbourne, Australia called Rosa Fennimore. My freelance business specialises in bridal and special occassions makeup.

I like the idea of having Rosa Fennimore in pink as its a feminine and soft colour. I would like a very clean, classy and simple (with an element of fun if that's possible) design. I would consider the business name to be in gloss with an otherwise matte finish.

Underneath the business name, I would like "Makeup by Tara Quillend"

I do not want any bridal related graphics.

Target Market(s)

Young females with a disposable income from ages 20-40 and females getting married who will dictate who does mother of bride makeup ages 40-70.

Industry/Entity Type

Business

Requirements
Must have
• "Makeup by Tara Quillend"

Ph: 0432 615 204
E: rosafennimore@examplemail.com
ABN: 58902147635
Nice to have
• I think I would like a mini business cards which is more slimline. I do like the colours of pink, white and grey but open to suggestions.
Should not have
• Bridal related graphics

```html
<!DOCTYPE html>
<html lang="en">
<head>
<meta charset="utf-8">
<title>Rosa Fennimore — Business Card</title>
<link rel="stylesheet" href="https://fonts.googleapis.com/css2?family=Great+Vibes&family=Courier+Prime:wght@400;700&display=swap">
<style>
  :root {
    --pink: #e6237a;
    --pink-deep: #c81866;
    --charcoal: #2d2d2f;
    --white: #ffffff;
  }
  html, body {
    margin: 0;
    padding: 0;
    width: 1200px;
    height: 521px;
    overflow: hidden;
    background: var(--charcoal);
  }
  .card {
    position: relative;
    width: 1200px;
    height: 521px;
    background: var(--charcoal);
    overflow: hidden;
    font-family: "Courier Prime", "Courier New", monospace;
  }
  .card__band {
    position: absolute;
    left: 0;
    top: 0;
    width: 1200px;
    height: 280px;
  }
  .card__kiss {
    position: absolute;
    left: 975px;
    top: 42px;
    width: 190px;
    height: 120px;
  }
  .brand {
    position: absolute;
    left: 48px;
    top: 2px;
    margin: 0;
    font-weight: 400;
  }
  .brand__name {
    display: block;
    font-family: "Great Vibes", cursive;
    font-weight: 400;
    font-size: 152px;
    line-height: 1.1;
    color: var(--white);
    letter-spacing: 1px;
    white-space: nowrap;
  }
  .brand__tagline {
    display: block;
    margin: 0 0 0 12px;
    font-size: 28px;
    font-weight: 400;
    color: var(--white);
    letter-spacing: 0.5px;
    white-space: nowrap;
  }
  .contact {
    position: absolute;
    right: 72px;
    top: 334px;
    margin: 0;
    padding: 0;
    list-style: none;
    text-align: right;
    color: var(--white);
  }
  .contact__item {
    display: flex;
    justify-content: flex-end;
    align-items: center;
    gap: 12px;
    white-space: nowrap;
  }
  .contact__item--phone { font-size: 36px; height: 52px; }
  .contact__item--email { font-size: 27px; height: 56px; }
  .contact__item--abn { font-size: 30px; height: 58px; }
  .contact__icon { fill: var(--pink); flex: none; }
  .contact__label { color: var(--pink); }
</style>
</head>
<body>
  <main class="card">
    <svg class="card__band" viewBox="0 0 1200 280" aria-hidden="true">
      <defs>
        <pattern id="teeth" x="0" y="243" width="36.3636" height="33" patternUnits="userSpaceOnUse">
          <polygon points="0,0 36.3636,0 18.1818,33" fill="#e6237a"/>
        </pattern>
      </defs>
      <rect x="0" y="0" width="1200" height="244" fill="#e6237a"/>
      <rect x="0" y="243" width="1200" height="33" fill="url(#teeth)"/>
    </svg>

    <svg class="card__kiss" viewBox="0 0 190 120" role="img" aria-label="Lipstick kiss mark decoration">
      <ellipse cx="95" cy="60" rx="92" ry="54" fill="#c81866" opacity="0.75"/>
    </svg>

    <h1 class="brand">
      <span class="brand__name">Rosa Fennimore</span>
      <span class="brand__tagline">«makeup by Tara Quillend»</span>
    </h1>

    <ul class="contact">
      <li class="contact__item contact__item--phone">
        <svg class="contact__icon" width="28" height="28" viewBox="0 0 24 24" aria-hidden="true">
          <path d="M6.6 10.8a15.1 15.1 0 0 0 6.6 6.6l2.2-2.2c.3-.3.7-.4 1-.2 1.1.4 2.3.6 3.6.6.6 0 1 .4 1 1V20c0 .6-.4 1-1 1A17 17 0 0 1 3 4c0-.6.4-1 1-1h3.5c.6 0 1 .4 1 1 0 1.3.2 2.5.6 3.6.1.3 0 .7-.2 1z"/>
        </svg>
        <span>0432 615 204</span>
      </li>
      <li class="contact__item contact__item--email">
        <svg class="contact__icon" width="28" height="22" viewBox="0 0 28 22" aria-hidden="true">
          <path d="M0 2l14 9 14-9V0H0z"/>
          <path d="M0 5v17h28V5L14 14z"/>
        </svg>
        <span>rosafennimore@examplemail.com</span>
      </li>
      <li class="contact__item contact__item--abn">
        <span><span class="contact__label">abn</span> 58902147635</span>
      </li>
    </ul>
  </main>
</body>
</html>
```